2 Wine Label Designs

Amberly Cellars has been helping people give customized wine gifts since 1999. From large scale corporate clients, to 1 bottle personalized gifts, we offer a wide range of wines and templates for any occasion. Recently we’ve started to shift our focus to a younger demographic (21 to 35 year old women) and are in the process of updating our website and branding.

One big area we’re working to improve is the customizable wine label/engraving templates we offer on the site (to see our current template library go to www.amberlycellars.com/shop/wine, select a wine, choose “label” or “engraving” from the dropdown, and click “customize”). You’ll find that a lot of our current templates are outdated or aimed at an older demographic. Over the next few months we want to swap out most of these old templates with fun fresh designs.

We're asking designers to submit 2 customizable wine label templates for this project. One should be wedding themed and the other "Thank You" themed. Please see the attached PDF for more guidelines and creative direction.

Keep in mind, even if you aren't selected as the winner of this project we are going to go through and offer $50 for any label template submitted that we like ($100 if we want both). So there is a good chance you'll be getting some money for your work!

Please read though the attached guidelines PDF carefully (especially the "Must be Customizable" section).

Target Market(s)

21 to 35 year old women

Colors

Designer to choose colors to be used in the design.

Requirements
Must have
• See attached PDF
Nice to have
• See attached PDF
Should not have
• See attached PDF

```html
<!DOCTYPE html>
<html lang="en">
<head>
<meta charset="utf-8">
<title>Thank You Wine Label Templates</title>
<link rel="stylesheet" href="https://fonts.googleapis.com/css2?family=Nunito:wght@500&family=Old+Standard+TT&family=Playball&display=swap">
<style>
  :root {
    --page: #ffffff;
    --heading: #1c1c1c;
    --ink: #7a3a22;
    --frame-dark: #6b5551;
    --frame-tan: #c9a27f;
    --cream: #fdf8ec;
    --paper-light: #f8f0e4;
    --paper-mid: #ead9c3;
    --paper-edge: #d8bfa2;
    --ornament-strong: rgba(122, 58, 34, 0.20);
    --ornament-soft: rgba(122, 58, 34, 0.07);
  }
  * { margin: 0; padding: 0; box-sizing: border-box; }
  html, body { width: 1200px; height: 1200px; overflow: hidden; background: var(--page); }
  .sheet { position: relative; width: 1200px; height: 1200px; }

  .template-title {
    position: absolute;
    font-family: "Nunito", sans-serif;
    font-weight: 500;
    font-size: 42px;
    letter-spacing: 0.13em;
    color: var(--heading);
    transform: translateX(-50%);
    white-space: nowrap;
    line-height: 1;
  }
  .title-wide { left: 862px; top: 66px; }
  .title-tall { left: 274px; top: 262px; }
  .title-square { left: 301px; top: 1087px; }

  .label {
    position: absolute;
    background: radial-gradient(ellipse at 50% 45%, var(--paper-light) 0%, var(--paper-mid) 62%, var(--paper-edge) 100%);
    overflow: hidden;
  }
  .label-tall { left: 27px; top: 320px; width: 490px; height: 630px; }
  .label-wide { left: 550px; top: 119px; width: 622px; height: 483px; }
  .label-square { left: 550px; top: 644px; width: 484px; height: 484px; }

  .frame-lines { position: absolute; inset: 0; width: 100%; height: 100%; }
  .frame-lines .rule { stroke: var(--ink); stroke-width: 2; fill: none; }
  .frame-lines .dots { stroke: var(--ink); stroke-width: 2; stroke-dasharray: 0.1 5; stroke-linecap: round; fill: none; }

  /* soft placeholder tone for the scrolling corner flourishes; fades fully inside its box */
  .corner-flourish {
    position: absolute;
    background: radial-gradient(closest-side, var(--ornament-strong) 0%, var(--ornament-soft) 55%, rgba(122, 58, 34, 0) 100%);
  }

  .name-panel { position: absolute; }
  .name-panel svg { position: absolute; inset: 0; width: 100%; height: 100%; }
  .panel-outer { fill: var(--frame-dark); }
  .panel-band { fill: var(--frame-tan); }
  .panel-face { fill: var(--cream); }
  .panel-dots { fill: none; stroke: var(--frame-tan); stroke-width: 2.2; stroke-dasharray: 0.1 6; stroke-linecap: round; }

  .panel-flourish {
    position: absolute;
    width: 14%; height: 14%;
    background: radial-gradient(closest-side, rgba(122, 58, 34, 0.22) 0%, rgba(122, 58, 34, 0.08) 55%, rgba(122, 58, 34, 0) 100%);
  }
  .pf-tl { left: 4%; top: 4%; }
  .pf-tr { right: 4%; top: 4%; }
  .pf-bl { left: 4%; bottom: 4%; }
  .pf-br { right: 4%; bottom: 4%; }

  .panel-copy {
    position: absolute;
    inset: 0;
    display: flex;
    flex-direction: column;
    align-items: center;
    color: var(--ink);
  }
  .thank-you {
    font-family: "Playball", cursive;
    font-weight: 400;
    line-height: 0.88;
    text-align: center;
  }
  .tagline, .tagline-sub {
    font-family: "Old Standard TT", serif;
    display: flex;
    align-items: center;
    white-space: nowrap;
    letter-spacing: 0.01em;
  }
  .tagline::before, .tagline::after,
  .tagline-sub::before, .tagline-sub::after {
    content: "";
    display: block;
    height: 1.5px;
    background: var(--ink);
  }
  .tagline::before, .tagline::after { width: 30px; margin: 0 4px; }
  .tagline-sub::before, .tagline-sub::after { width: 22px; margin: 0 4px; }

  .couple-text {
    position: absolute;
    left: 0; right: 0;
    text-align: center;
    font-family: "Playball", cursive;
    color: var(--ink);
    line-height: 1.3;
  }

  .panel-lg { width: 324px; height: 300px; }
  .panel-lg .panel-copy { padding-top: 38px; }
  .panel-lg .thank-you { font-size: 74px; }
  .panel-lg .tagline { font-size: 12.5px; margin-top: 16px; }
  .panel-lg .tagline-sub { font-size: 12px; margin-top: 4px; }

  .panel-sm { width: 280px; height: 258px; }
  .panel-sm .panel-copy { padding-top: 32px; }
  .panel-sm .thank-you { font-size: 64px; }
  .panel-sm .tagline { font-size: 11px; margin-top: 14px; }
  .panel-sm .tagline-sub { font-size: 10.5px; margin-top: 3px; }
  .panel-sm .tagline::before, .panel-sm .tagline::after { width: 24px; }
</style>
</head>
<body>
<main class="sheet">

  <h2 class="template-title title-wide">WIDE TEMPLATE</h2>
  <h2 class="template-title title-tall">TALL TEMPLATE</h2>
  <h2 class="template-title title-square">SQUARE TEMPLATE</h2>

  <section class="label label-tall">
    <svg class="frame-lines" viewBox="0 0 490 630">
      <line class="rule" x1="177" y1="30" x2="461" y2="30"/>
      <line class="dots" x1="183" y1="36" x2="455" y2="36"/>
      <line class="rule" x1="461" y1="30" x2="461" y2="452"/>
      <line class="dots" x1="455" y1="36" x2="455" y2="446"/>
      <line class="rule" x1="29" y1="176" x2="29" y2="600"/>
      <line class="dots" x1="35" y1="182" x2="35" y2="594"/>
      <line class="rule" x1="29" y1="600" x2="309" y2="600"/>
      <line class="dots" x1="35" y1="594" x2="303" y2="594"/>
    </svg>
    <div class="corner-flourish" role="img" aria-label="Scrolling corner flourish ornament" style="left:12px; top:14px; width:160px; height:152px;"></div>
    <div class="corner-flourish" role="img" aria-label="Scrolling corner flourish ornament" style="left:320px; top:462px; width:162px; height:154px;"></div>

    <div class="name-panel panel-lg" style="left:81px; top:94px;">
      <svg viewBox="0 0 324 300" preserveAspectRatio="none">
        <path class="panel-outer" d="M28 0 H296 A28 28 0 0 0 324 28 V272 A28 28 0 0 0 296 300 H28 A28 28 0 0 0 0 272 V28 A28 28 0 0 0 28 0 Z"/>
        <path class="panel-band" d="M36.7 10 H287.3 A38 38 0 0 0 314 36.7 V263.3 A38 38 0 0 0 287.3 290 H36.7 A38 38 0 0 0 10 263.3 V36.7 A38 38 0 0 0 36.7 10 Z"/>
        <path class="panel-face" d="M39.6 14 H284.4 A42 42 0 0 0 310 39.6 V260.4 A42 42 0 0 0 284.4 286 H39.6 A42 42 0 0 0 14 260.4 V39.6 A42 42 0 0 0 39.6 14 Z"/>
        <path class="panel-dots" vector-effect="non-scaling-stroke" d="M46.1 24 H277.9 A52 52 0 0 0 300 46.1 V253.9 A52 52 0 0 0 277.9 276 H46.1 A52 52 0 0 0 24 253.9 V46.1 A52 52 0 0 0 46.1 24 Z"/>
      </svg>
      <div class="panel-flourish pf-tl" role="img" aria-label="Leaf corner ornament"></div>
      <div class="panel-flourish pf-tr" role="img" aria-label="Leaf corner ornament"></div>
      <div class="panel-flourish pf-bl" role="img" aria-label="Leaf corner ornament"></div>
      <div class="panel-flourish pf-br" role="img" aria-label="Leaf corner ornament"></div>
      <div class="panel-copy">
        <h1 class="thank-you">Thank<br>You</h1>
        <p class="tagline">CELEBRATE GOOD TIMES</p>
        <p class="tagline-sub">COME ON</p>
      </div>
    </div>

    <p class="couple-text" style="top:440px; font-size:36px;">“Couple<br>Text Here”</p>
  </section>

  <section class="label label-wide">
    <svg class="frame-lines" viewBox="0 0 622 483">
      <line class="rule" x1="174" y1="30" x2="595" y2="30"/>
      <line class="dots" x1="180" y1="36" x2="589" y2="36"/>
      <line class="rule" x1="595" y1="30" x2="595" y2="305"/>
      <line class="dots" x1="589" y1="36" x2="589" y2="299"/>
      <line class="rule" x1="30" y1="173" x2="30" y2="455"/>
      <line class="dots" x1="36" y1="179" x2="36" y2="449"/>
      <line class="rule" x1="30" y1="455" x2="446" y2="455"/>
      <line class="dots" x1="36" y1="449" x2="440" y2="449"/>
    </svg>
    <div class="corner-flourish" role="img" aria-label="Scrolling corner flourish ornament" style="left:14px; top:12px; width:152px; height:154px;"></div>
    <div class="corner-flourish" role="img" aria-label="Scrolling corner flourish ornament" style="left:458px; top:316px; width:150px; height:154px;"></div>

    <div class="name-panel panel-lg" style="left:150px; top:55px;">
      <svg viewBox="0 0 324 300" preserveAspectRatio="none">
        <path class="panel-outer" d="M28 0 H296 A28 28 0 0 0 324 28 V272 A28 28 0 0 0 296 300 H28 A28 28 0 0 0 0 272 V28 A28 28 0 0 0 28 0 Z"/>
        <path class="panel-band" d="M36.7 10 H287.3 A38 38 0 0 0 314 36.7 V263.3 A38 38 0 0 0 287.3 290 H36.7 A38 38 0 0 0 10 263.3 V36.7 A38 38 0 0 0 36.7 10 Z"/>
        <path class="panel-face" d="M39.6 14 H284.4 A42 42 0 0 0 310 39.6 V260.4 A42 42 0 0 0 284.4 286 H39.6 A42 42 0 0 0 14 260.4 V39.6 A42 42 0 0 0 39.6 14 Z"/>
        <path class="panel-dots" vector-effect="non-scaling-stroke" d="M46.1 24 H277.9 A52 52 0 0 0 300 46.1 V253.9 A52 52 0 0 0 277.9 276 H46.1 A52 52 0 0 0 24 253.9 V46.1 A52 52 0 0 0 46.1 24 Z"/>
      </svg>
      <div class="panel-flourish pf-tl" role="img" aria-label="Leaf corner ornament"></div>
      <div class="panel-flourish pf-tr" role="img" aria-label="Leaf corner ornament"></div>
      <div class="panel-flourish pf-bl" role="img" aria-label="Leaf corner ornament"></div>
      <div class="panel-flourish pf-br" role="img" aria-label="Leaf corner ornament"></div>
      <div class="panel-copy">
        <h1 class="thank-you">Thank<br>You</h1>
        <p class="tagline">CELEBRATE GOOD TIMES</p>
        <p class="tagline-sub">COME ON</p>
      </div>
    </div>

    <p class="couple-text" style="top:378px; font-size:38px;">“Couple Text Here”</p>
  </section>

  <section class="label label-square">
    <svg class="frame-lines" viewBox="0 0 484 484">
      <line class="rule" x1="138" y1="20" x2="464" y2="20"/>
      <line class="dots" x1="144" y1="26" x2="458" y2="26"/>
      <line class="rule" x1="464" y1="20" x2="464" y2="356"/>
      <line class="dots" x1="458" y1="26" x2="458" y2="350"/>
      <line class="rule" x1="24" y1="136" x2="24" y2="464"/>
      <line class="dots" x1="30" y1="142" x2="30" y2="458"/>
      <line class="rule" x1="24" y1="464" x2="346" y2="464"/>
      <line class="dots" x1="30" y1="458" x2="340" y2="458"/>
    </svg>
    <div class="corner-flourish" role="img" aria-label="Scrolling corner flourish ornament" style="left:8px; top:10px; width:126px; height:144px;"></div>
    <div class="corner-flourish" role="img" aria-label="Scrolling corner flourish ornament" style="left:354px; top:350px; width:124px; height:126px;"></div>

    <div class="name-panel panel-sm" style="left:102px; top:58px;">
      <svg viewBox="0 0 324 300" preserveAspectRatio="none">
        <path class="panel-outer" d="M28 0 H296 A28 28 0 0 0 324 28 V272 A28 28 0 0 0 296 300 H28 A28 28 0 0 0 0 272 V28 A28 28 0 0 0 28 0 Z"/>
        <path class="panel-band" d="M36.7 10 H287.3 A38 38 0 0 0 314 36.7 V263.3 A38 38 0 0 0 287.3 290 H36.7 A38 38 0 0 0 10 263.3 V36.7 A38 38 0 0 0 36.7 10 Z"/>
        <path class="panel-face" d="M39.6 14 H284.4 A42 42 0 0 0 310 39.6 V260.4 A42 42 0 0 0 284.4 286 H39.6 A42 42 0 0 0 14 260.4 V39.6 A42 42 0 0 0 39.6 14 Z"/>
        <path class="panel-dots" vector-effect="non-scaling-stroke" d="M46.1 24 H277.9 A52 52 0 0 0 300 46.1 V253.9 A52 52 0 0 0 277.9 276 H46.1 A52 52 0 0 0 24 253.9 V46.1 A52 52 0 0 0 46.1 24 Z"/>
      </svg>
      <div class="panel-flourish pf-tl" role="img" aria-label="Leaf corner ornament"></div>
      <div class="panel-flourish pf-tr" role="img" aria-label="Leaf corner ornament"></div>
      <div class="panel-flourish pf-bl" role="img" aria-label="Leaf corner ornament"></div>
      <div class="panel-flourish pf-br" role="img" aria-label="Leaf corner ornament"></div>
      <div class="panel-copy">
        <h1 class="thank-you">Thank<br>You</h1>
        <p class="tagline">CELEBRATE GOOD TIMES</p>
        <p class="tagline-sub">COME ON</p>
      </div>
    </div>

    <p class="couple-text" style="top:362px; font-size:34px;">“Couple Text Here”</p>
  </section>

</main>
</body>
</html>
```